Informative 1-Pager website that informs users about the threat of ransomware

See current page: https://www.brixlo-vantel.com/

Coding

Coded - Design and coding required

```html
<!DOCTYPE html>
<html lang="en">
<head>
<meta charset="utf-8">
<title>Protect from ransomware</title>
<link href="https://fonts.googleapis.com/css2?family=Manrope:wght@400;500;600;700&display=swap" rel="stylesheet">
<style>
:root{
  --navy:#0b1a33;
  --navy-deep:#07122a;
  --ink:#14213d;
  --text:#1c2335;
  --muted:#6b7080;
  --accent:#e0ab1c;
  --button:#f6c02d;
  --numbers:#1f3b70;
  --grey:#eceef2;
  --card:#f6f6f7;
  --white:#ffffff;
}
*{margin:0;padding:0;box-sizing:border-box}
html,body{width:1200px;height:4149px;overflow:hidden}
body{position:relative;background:var(--white);font-family:"Manrope",sans-serif;color:var(--text)}
.abs{position:absolute}
.accent{color:var(--accent)}
h1,h2{font-weight:400;color:var(--ink);letter-spacing:-0.3px}

/* header + hero */
.brand{left:106px;top:18px;font-size:16px;font-weight:700;line-height:19px;color:var(--ink)}
.nav{top:28px;font-size:10px;color:var(--ink)}
.nav.home{left:480px;padding-bottom:5px;border-bottom:1px solid var(--ink)}
.nav.contact{left:525px}
.hero-title{left:106px;top:196px;font-size:50px;line-height:57px;width:460px}
.hero-sub{left:106px;top:393px;width:390px;font-size:12px;line-height:21px;color:var(--muted)}
.btn{display:flex;align-items:center;justify-content:center;background:var(--button);border-radius:5px;font-size:12px;font-weight:600;color:var(--ink)}
.hero-btn{left:106px;top:462px;width:214px;height:46px}
.scroll-arrow{left:566px;top:618px}
.hero-visual{left:600px;top:0;width:600px;height:674px;background:radial-gradient(circle at 62% 42%,#b9d2f2 0%,#5877c4 18%,#2a3f92 42%,#1b2460 65%,#7d4a6a 88%,#c06a4a 100%)}

/* nutshell */
.band{left:0;top:674px;width:1200px;height:288px;background:linear-gradient(110deg,#123059 0%,var(--navy) 40%,var(--navy-deep) 100%)}
.band-title{left:190px;top:728px;font-size:36px;line-height:48px;color:var(--white);font-weight:400}
.band-text{left:506px;top:746px;width:510px;font-size:12px;line-height:19px;color:var(--white);font-weight:500}
.video{left:195px;top:855px;width:810px;height:405px;border-radius:6px;overflow:hidden;background:radial-gradient(circle at 50% 55%,#2f8df2 0%,#1d3f7a 12%,#3a2620 32%,#221510 70%,#120b08 100%);box-shadow:0 16px 34px rgba(0,0,0,.22)}
.video-label{left:38px;top:12px;font-size:11px;color:var(--white)}
.video-dot{left:12px;top:10px;width:20px;height:20px;border-radius:50%;background:#c7255c}
.video-play{left:385px;top:186px}

/* section headings */
.center-head{left:0;width:1200px;text-align:center;font-size:36px;line-height:46px}
.center-sub{left:0;width:1200px;text-align:center;font-size:11px;color:var(--muted)}

/* types */
.type{width:160px}
.type svg{display:block;margin-bottom:44px}
.type h3,.step h3,.item h3{font-size:12px;font-weight:500;line-height:19px;color:var(--ink);margin-bottom:10px}
.type p,.step p,.item p{font-size:9.5px;line-height:15px;color:var(--muted)}

/* what if */
.whatif-title{left:227px;top:1846px;font-size:50px;line-height:56px;width:360px}
.whatif-col{left:638px;top:1844px;width:395px}
.stage-label{font-size:9px;color:var(--numbers);margin-bottom:4px}
.stage h3{font-size:12.5px;font-weight:500;line-height:20px;color:var(--ink);margin-bottom:14px}
.stage p{font-size:10px;line-height:17px;color:var(--muted)}
.stage+.stage{margin-top:34px}
.read-more{display:block;margin-top:28px;font-size:10px;color:var(--numbers);font-weight:600}

/* infected */
.grey{left:0;top:2360px;width:1200px;height:537px;background:linear-gradient(100deg,#f5f3ef 0%,var(--grey) 45%,#e6e9ee 100%)}
.infected-title{left:122px;top:2444px;font-size:36px;line-height:46px;width:320px}
.item{width:270px}
.item svg{display:block;margin-bottom:26px}

/* avoid */
.step{width:165px}
.step .num{font-size:36px;line-height:40px;color:var(--numbers);margin-bottom:8px;display:block}

/* darknet + form */
.dark-title{left:147px;top:3566px;font-size:36px;line-height:48px;width:430px}
.dark-text{left:147px;top:3716px;width:345px;font-size:10px;line-height:17px;color:var(--muted)}
.footer{left:0;top:3861px;width:1200px;height:288px;background:radial-gradient(circle at 80% 30%,#122a52 0%,var(--navy) 45%,var(--navy-deep) 100%)}
.form-card{left:609px;top:3483px;width:485px;height:448px;background:var(--card);border-radius:4px;box-shadow:0 10px 30px rgba(0,0,0,.06)}
.form-title{left:45px;top:48px;font-size:24px;color:var(--ink);font-weight:400}
.field{left:45px;width:395px;background:var(--white);border-radius:3px;font-size:10px;color:var(--muted);padding:20px 16px}
.field.email{top:106px;height:55px}
.field.message{top:175px;height:170px;padding-top:20px}
.submit{left:314px;top:375px;width:126px;height:47px}

/* footer */
.footer-brand{left:147px;top:3897px;font-size:16px;font-weight:700;line-height:19px;color:var(--white)}
.about-title{left:147px;top:3978px;font-size:36px;color:var(--white);font-weight:400}
.about-text{left:147px;top:4040px;width:510px;font-size:10px;line-height:16px;color:#c9cfdc}
.social{top:4055px;width:30px;height:30px;border-radius:50%;border:2px solid var(--button)}
</style>
</head>
<body>

<div class="abs brand">Protect from<br>ransomware</div>
<div class="abs nav home">Home</div>
<div class="abs nav contact">Contact us</div>
<h1 class="abs hero-title">Learn how to protect yourself from ransomware</h1>
<p class="abs hero-sub">Keep your computer safe and understand how to act in case of an successful attack</p>
<div class="abs btn hero-btn">Get in contact with us</div>
<svg class="abs scroll-arrow" width="14" height="36" viewBox="0 0 14 36"><path d="M7 0V34M1 28l6 6 6-6" stroke="#14213d" stroke-width="1.2" fill="none"/></svg>
<div class="abs hero-visual" role="img" aria-label="Close-up of a human eye overlaid with glowing blue circuit lines"></div>

<div class="abs band"></div>
<h2 class="abs band-title">Ransomware<br>in a nutshell</h2>
<p class="abs band-text">Ransomware is a very dangerous cyber threat to all organisations and individuals. Ransomware is a type of malicious software that may block access to files or devices until the victim pays a ransom.The ransom is usually demanded in cryptocurrency.</p>
<div class="abs video" role="img" aria-label="Video thumbnail: world map with red location pins around a glowing padlock">
  <div class="abs video-dot"></div>
  <div class="abs video-label">Ransomware</div>
  <svg class="abs video-play" width="40" height="40" viewBox="0 0 40 40"><circle cx="20" cy="20" r="20" fill="rgba(255,255,255,.9)"/><path d="M16 12l12 8-12 8z" fill="#14213d"/></svg>
</div>

<h2 class="abs center-head" style="top:1333px">What are common ransomware <span class="accent">types?</span></h2>
<p class="abs center-sub" style="top:1398px">There are many different types of ransomware. Here are four typical categories:</p>

<div class="abs type" style="left:158px;top:1463px">
  <svg width="44" height="44" viewBox="0 0 44 44" fill="none" stroke="#1f3b70" stroke-width="1.5"><rect x="2" y="2" width="16" height="11"/><rect x="26" y="30" width="16" height="11"/><circle cx="22" cy="22" r="6"/><path d="M10 13v9h6M34 30v-8h-6"/></svg>
  <h3>Ransomware that<br>fakes something</h3>
  <p>Scareware fakes a problem on the computer. For example, it could be a warning that a virus or malware has been found on the PC. The software then redirects the user to a website where the problem can be solved for a fee.</p>
</div>
<div class="abs type" style="left:401px;top:1463px">
  <svg width="44" height="44" viewBox="0 0 44 44" fill="none" stroke="#1f3b70" stroke-width="1.5"><rect x="4" y="20" width="18" height="20" rx="2"/><path d="M8 20v-5a5 5 0 0 1 10 0v5"/><circle cx="13" cy="30" r="3"/><path d="M26 4h4v4h-4zM34 4h4v4h-4zM30 10h4v4h-4zM38 12h4v4h-4zM26 16h4v4h-4z"/></svg>
  <h3>Ransomware that<br>encrypts something:</h3>
  <p>Encryptors are the most common type of ransomware that encrypts all data and requires a key to unlock it, which can usually be purchased within a short period of time.</p>
</div>
<div class="abs type" style="left:643px;top:1463px">
  <svg width="44" height="44" viewBox="0 0 44 44" fill="none" stroke="#1f3b70" stroke-width="1.5"><path d="M22 6l14 5v10c0 9-6 15-14 18C14 36 8 30 8 21V11z"/><path d="M16 22l5 5 8-9"/><path d="M32 2h3v3h-3zM38 6h3v3h-3zM34 10h3v3h-3z"/></svg>
  <h3>Ransomware that<br>leaks data</h3>
  <p>This type of ransomware is called Doxware. Doxware often tries to force the user or the company to pay by threatening to publish confidential information online at a "Hall of Shame".</p>
</div>
<div class="abs type" style="left:886px;top:1463px">
  <svg width="44" height="44" viewBox="0 0 44 44" fill="none" stroke="#1f3b70" stroke-width="1.5"><rect x="2" y="10" width="32" height="24" rx="2"/><path d="M12 40h12M18 34v6"/><circle cx="34" cy="10" r="8"/><rect x="31" y="9" width="6" height="5"/><path d="M32 9V7a2 2 0 0 1 4 0v2"/><circle cx="18" cy="22" r="5"/></svg>
  <h3>Ransomware that<br>locks something</h3>
  <p>Instead of preventing access to files or applications, this ransomware type prevent the end user's device from being used. For example, key combinations (CTRL +ALT+DEL) are also locked, so that the user can no longer access his current work. Usually, details of the ransomware are displayed on the lock screen.</p>
</div>

<h2 class="abs whatif-title">What if you <span class="accent">don't pay</span> the ransom?</h2>
<svg class="abs" style="left:430px;top:1980px" width="155" height="152" viewBox="0 0 155 152"><path d="M2 150L153 2" stroke="#e0ab1c" stroke-width="1" opacity=".6"/></svg>
<div class="abs whatif-col">
  <div class="stage">
    <div class="stage-label">STAGE 01</div>
    <h3>If one does not pay the ransom and has no backup, the data is usually lost forever.</h3>
    <p>Sometimes, however, the data ends up on the dark web and the affected companies are exposed. Thus, it is not the loss of the data that is the angle with which the hackers build up pressure, but the reputation damage caused by the lost data. This damage can be much greater than the value of the individual data. For example, who wants to do business with a bank that can't even protect itself? Every potential customer will not weigh his own money in security and go to a competitor</p>
  </div>
  <div class="stage">
    <div class="stage-label">STAGE 02</div>
    <h3>In the darknet, some hacker collectives operate websites where the attacked companies are exposed at a "hall of shame".</h3>
    <p>This is where the complete data sets are published for everyone to see. By using free download links, all data can then also be downloaded immediately. Often, these data sets contain personal information about employees. Such a violation of privacy due to insufficient protection can lead to high penalties due to legal requirements such as GDPR. But unfortunately, the data leaks also often affect customers and partners of the involved organization, depending on the position of the employee who was hacked.</p>
  </div>
  <span class="read-more">READ MORE →</span>
</div>

<div class="abs grey"></div>
<h2 class="abs infected-title">How can you <span class="accent">get infected</span> by ransomware?</h2>
<div class="abs item" style="left:491px;top:2448px">
  <svg width="42" height="44" viewBox="0 0 42 44" fill="none" stroke="#1f3b70" stroke-width="1.5"><rect x="2" y="2" width="38" height="30" rx="2"/><path d="M21 8l9 16H12z M21 14v5M21 21v1"/><path d="M6 40h6M18 40h6M30 40h6M9 32v8M33 32v8"/></svg>
  <h3>Infection by ransomware usually occurs through interaction with a user</h3>
  <p>For example, an attacker might send an email with an attachment containing the malware or download it from the Internet downstream. Usually, such malware is distributed as part of phishing attacks.</p>
</div>
<div class="abs item" style="left:815px;top:2448px">
  <svg width="42" height="44" viewBox="0 0 42 44" fill="none" stroke="#1f3b70" stroke-width="1.5"><path d="M10 30a8 8 0 0 1 0-16 11 11 0 0 1 21-2 8 8 0 0 1 1 18z"/><circle cx="21" cy="21" r="6"/><path d="M21 18v6M18 21l3 3 3-3M8 36h26M12 42h18"/></svg>
  <h3>But there are many other ways how the malware can get onto the PC.</h3>
  <p>The hacker can also hide the malware in downloads on websites. For this purpose, the criminal can create websites himself, which are very similar to a regular reputable websites. Using freely available tools, complete websites can be easily even cloned and thanks to typosquatting technique, the corresponding domains can be purchased as well.</p>
</div>
<div class="abs item" style="left:491px;top:2670px">
  <svg width="44" height="44" viewBox="0 0 44 44" fill="none" stroke="#1f3b70" stroke-width="1.5"><path d="M20 4l14 5v10c0 9-6 15-14 18C12 34 6 28 6 19V9z"/><path d="M14 18l4 4 8-8"/><circle cx="34" cy="34" r="7"/><path d="M31 31l6 6M37 31l-6 6"/></svg>
  <h3>However, the possibilities to bring malware onto a PC are even more diverse.</h3>
  <p>These include bad USB attacks, unpatched browsers or plugins that enable drive-by attacks, hacker-controlled banner ads on regular websites, malicious links on social media platforms and many more.</p>
</div>

<h2 class="abs center-head" style="top:3002px">How can you avoid<br>a ransomware <span class="accent">attack?</span></h2>
<p class="abs center-sub" style="top:3094px">Thebest defense is the right behavior.</p>

<div class="abs step" style="left:143px;top:3158px">
  <span class="num">01</span>
  <h3>Be suspicious of all downloads, attachments, etc.</h3>
  <p>And only run software if you trust the creator. This includes macros in office applications.</p>
</div>
<div class="abs step" style="left:393px;top:3158px">
  <span class="num">02</span>
  <h3>Also, keep your operating system and all applications patched and up to date</h3>
  <p>To ensure that you have fewer vulnerabilities that a hacker can exploit. Also, make sure that you are a regular user with minimal privileges and are not also an administrator.</p>
</div>
<div class="abs step" style="left:644px;top:3158px">
  <span class="num">03</span>
  <h3>Install antivirus software that detects malicious programs</h3>
  <p>Like ransomware and enable all security features offered by the operating system (e.g. Guardis in Orbix OS).</p>
</div>
<div class="abs step" style="left:894px;top:3158px">
  <span class="num">04</span>
  <h3>And of course, back up your files regularly and automatically!</h3>
  <p>This won't prevent a ransomware attack, but it can significantly reduce the damage caused by such an attack.</p>
</div>

<h2 class="abs dark-title">How do you know if your data might be already exposed <span class="accent">in the darknet?</span></h2>
<p class="abs dark-text">Navetra offers a service that will find leaked data or your organisation mentioned on "ransomware hall of shame websites".</p>

<div class="abs footer"></div>
<div class="abs form-card">
  <h2 class="abs form-title">WANT TO KNOW MORE?</h2>
  <div class="abs field email">Your email</div>
  <div class="abs field message">Message</div>
  <div class="abs btn submit">Submit</div>
</div>
<div class="abs footer-brand">Protect from<br>ransomware</div>
<h2 class="abs about-title">About us</h2>
<p class="abs about-text">Navetra (company registration number CHE-418.207.596) was started in 2018 as a public limited company in Marvik, Lorania. Our analysts have long-standing relationships with various players on the Darknet. These personal relationships make it possible for Navetra to repeatedly obtain the latest data leaks. Those unique data leaks are published by the press around the world.</p>
<div class="abs social" style="left:1019px"></div>
<div class="abs social" style="left:1063px"></div>

</body>
</html>
```